www.norvatepastimes.com

Updating website so looks futristic but yet business like and easy to navigate, essentially a good landing page with a cool picture summing up what we do, and links to the following pages, all other pages on site to be updated, Exclusive Distributor of Brimla Flex Unique Fitness Equipment Products in UK & Ireland, www.ferncrestdash.co.uk Exclusive Partners & Distributors Of Ferncrest Dash - Obstacle Races - Obstacle Hire - Obstacle Training - Adventure Events, www.jogvelmora.co.uk Adventures That Inspire. We also Health Club / Facillity Consultancy

```html
<!DOCTYPE html>
<html lang="en">
<head>
<meta charset="utf-8">
<title>Norvate Pastimes – Health, Wellness, Fitness, Consultants</title>
<link href="https://fonts.googleapis.com/css2?family=Open+Sans:wght@300;400;600;700;800&display=swap" rel="stylesheet">
<style>
:root{
  --teal:#66c9b4;
  --teal-dark:#4fb59f;
  --ink:#222;
  --text:#555;
  --muted:#8a8a8a;
  --line:#e3e3e3;
  --black:#151515;
  --dark:#1f1f1f;
  --footer:#1b1b1b;
  --white:#fff;
  --soft:#eeeeee;
}
*{box-sizing:border-box;margin:0;padding:0}
html,body{width:1200px;height:4082px;overflow:hidden;background:var(--white)}
body{font-family:'Open Sans',Arial,sans-serif;color:var(--text)}
.canvas{position:relative;width:1200px;height:4082px;overflow:hidden}
section,header,footer{position:absolute;left:0;width:1200px;overflow:hidden}
.abs{position:absolute}

/* nav */
.site-header{top:0;height:95px;background:var(--white);box-shadow:0 1px 4px rgba(0,0,0,.08);z-index:2}
.brand{left:45px;top:8px}
.brand-name{font-size:40px;font-weight:300;color:var(--ink);line-height:1.1}
.brand-tag{font-size:15px;color:var(--teal);margin-top:2px}
.main-nav{left:443px;top:0;height:95px;display:flex}
.main-nav a{display:flex;align-items:center;height:95px;padding:0 17px;font-size:13px;font-weight:700;color:var(--ink);text-decoration:none;text-transform:uppercase}
.main-nav a.active{background:var(--teal);color:var(--white);padding:0 26px}

/* hero */
.hero{top:95px;height:563px;background:linear-gradient(90deg,#f3f1ef 0%,#e2ddd8 40%,#b9a9a0 70%,#8c7e77 100%)}
.hero-photo{left:380px;top:0;width:820px;height:563px;background:radial-gradient(ellipse at 60% 40%,#d7c2b4 0%,#b39c8d 35%,rgba(150,130,120,.2) 75%)}
.hero-title{left:46px;top:188px;font-size:46px;font-weight:400;color:var(--ink)}
.hero-sub{left:46px;top:240px;font-size:58px;font-weight:700;color:var(--teal);letter-spacing:1px}
.hero-line{left:46px;top:315px;font-size:32px;color:var(--ink)}
.btn-outline{display:flex;align-items:center;justify-content:center;border:2px solid var(--ink);font-size:13px;font-weight:600;text-transform:uppercase;color:var(--ink)}
.hero .btn-outline{left:46px;top:392px;width:152px;height:42px;background:rgba(255,255,255,.5)}

/* about */
.about{top:658px;height:476px}
.about-dark{left:0;top:0;width:620px;height:476px;background:var(--black)}
.about-photo{left:82px;top:20px;width:220px;height:456px;background:linear-gradient(180deg,#5a2e4a 0%,#7a5048 35%,#3a2a28 70%,#1a1a1a 100%);border-radius:100px 100px 0 0}
.story-small{left:300px;top:132px;width:275px;text-align:right;font-size:26px;color:#ddd;font-weight:300}
.story-big{left:300px;top:172px;width:275px;text-align:right;font-size:42px;font-weight:700;color:var(--white);letter-spacing:2px}
.about-teal{left:620px;top:0;width:580px;height:476px;background:var(--teal)}
.about-title{left:28px;top:36px;font-size:46px;font-weight:700;color:var(--white)}
.about-text{left:28px;top:114px;width:520px;font-size:14px;line-height:21px;color:var(--white)}
.about-text p+p{margin-top:18px}
.about-teal .btn-outline{left:33px;top:397px;width:142px;height:40px;border-color:var(--white);color:var(--white)}

/* bmi */
.bmi{top:1134px;height:601px;background:var(--white)}
.section-head{font-size:27px;font-weight:700;color:var(--ink);letter-spacing:1px;text-transform:uppercase}
.bmi .section-head{left:68px;top:38px}
.bmi-card{left:68px;top:96px;width:414px;height:470px;border:1px solid var(--line);box-shadow:0 0 6px rgba(0,0,0,.05)}
.tab{top:16px;height:38px;width:114px;display:flex;align-items:center;justify-content:center;font-size:13px}
.tab-male{left:26px;background:#f0f0f0;color:var(--text)}
.tab-female{left:140px;background:var(--teal);color:var(--white)}
.field{height:36px;border:1px solid #ddd;font-size:11px;color:#aaa;display:flex;align-items:center;padding-left:10px;background:var(--white)}
.unit{font-size:13px;font-weight:600;color:var(--ink)}
.select{width:310px}
.select::after{content:"";position:absolute;right:12px;top:15px;border:4px solid transparent;border-top:5px solid #444}
.info-dot{width:16px;height:16px;border-radius:50%;background:var(--teal)}
.btn-slant{left:26px;top:408px;width:168px;height:40px;background:var(--teal);color:var(--white);font-size:13px;font-weight:700;display:flex;align-items:center;padding-left:28px;clip-path:polygon(0 0,100% 0,85% 100%,0 100%)}
.bmi-photo{left:640px;top:36px;width:560px;height:565px;background:radial-gradient(ellipse at 35% 55%,#7a4a33 0%,#a06c4c 30%,rgba(255,255,255,0) 60%),radial-gradient(ellipse at 75% 45%,#c9a58a 0%,#ddc0a8 25%,rgba(255,255,255,0) 55%),#fff}

/* services */
.services{top:1735px;height:680px;background:linear-gradient(180deg,#262626 0%,#1a1a1a 60%,#121212 100%)}
.services .section-head{left:0;width:1200px;top:40px;text-align:center;color:var(--white);font-size:31px}
.service-card{top:120px;width:258px;height:506px;border:1px solid #555;border-radius:129px}
.service-photo{left:20px;top:22px;width:218px;height:218px;border-radius:50%;border:3px solid #666}
.service-label{left:-1px;top:275px;width:258px;height:46px;background:var(--white);display:flex;align-items:center;justify-content:center;font-size:20px;font-weight:700;color:var(--ink);text-transform:uppercase}
.service-text{left:28px;top:340px;width:202px;text-align:center;font-size:12px;line-height:18px;color:var(--white);font-weight:600}

/* events */
.events{top:2415px;height:545px;background:var(--white)}
.events .section-head{left:0;width:1200px;top:52px;text-align:center;font-size:31px}
.head-rule{left:560px;top:100px;width:80px;height:3px;background:var(--teal)}
.event{top:145px;width:240px}
.event-photo{position:relative;height:174px}
.event-label{height:46px;background:var(--teal);color:var(--white);display:flex;align-items:center;justify-content:center;font-size:16px}
.event-meta{list-style:none;margin-top:12px}
.event-meta li{display:flex;align-items:center;gap:12px;height:36px;font-size:14px;color:var(--muted);border-bottom:1px solid #f0f0f0;padding-left:12px}
.event-meta svg{flex:none}

/* social */
.social{top:2960px;height:644px;background:linear-gradient(180deg,#f2f2f2 0%,#e1e1e1 100%)}
.social .section-head{left:0;width:1200px;top:36px;text-align:center;font-size:31px}
.social-col{top:112px;width:297px}
.social-title{font-size:15px;font-weight:700;color:var(--ink);letter-spacing:1px;margin-bottom:8px;display:flex;align-items:center;gap:8px}
.social-title i{display:inline-block;width:12px;height:12px;background:var(--ink)}
.widget{position:relative;height:435px;background:var(--white);border:1px solid #ddd;overflow:hidden}
.small{font-size:10px;line-height:14px;color:#444}
.tw-item{display:flex;gap:8px;padding:10px;border-bottom:1px solid #eee}
.avatar{flex:none;width:34px;height:34px;background:#8a6a9a}
.ig-grid{display:grid;grid-template-columns:repeat(3,1fr);gap:5px;padding:0 8px}
.ig-grid span{height:88px;background:linear-gradient(135deg,#b78d75,#4a4a52)}

/* subscribe */
.subscribe{top:3604px;height:82px;background:#262626}
.sub-label{left:68px;top:30px;font-size:14px;color:var(--white)}
.sub-field{left:204px;top:22px;width:436px;height:38px;background:#1c1c1c;font-size:11px;color:#777;display:flex;align-items:center;padding-left:10px}
.sub-plus{left:606px;top:29px;font-size:20px;color:#e2403a;font-weight:700}
.follow{left:805px;top:30px;font-size:14px;color:var(--white);display:flex;align-items:center;gap:14px}
.follow span.dot{width:12px;height:12px;border-radius:50%;background:#bbb;display:inline-block}

/* footer */
.site-footer{top:3686px;height:348px;background:var(--footer)}
.foot-brand{left:68px;top:48px;font-size:33px;font-weight:300;color:var(--white)}
.foot-tag{left:68px;top:92px;font-size:13px;font-weight:700;color:var(--white)}
.foot-about{left:68px;top:134px;width:290px;font-size:11px;line-height:18px;color:#aaa}
.foot-contact{left:68px;top:186px;font-size:11px;line-height:18px;color:#aaa}
.foot-contact dt{float:left;width:60px;clear:left}
.foot-divider{top:60px;width:1px;height:270px;background:#333}
.foot-head{font-size:14px;font-weight:600;color:var(--white);text-transform:uppercase}
.hours{left:449px;top:128px;width:290px;list-style:none;font-size:11px;color:#aaa}
.hours li{display:flex;justify-content:space-between;height:41px;border-bottom:1px dotted #444;align-items:center}
.hours-note{left:449px;top:254px;font-size:11px;color:#aaa}
.class-item{left:835px;display:flex;gap:14px}
.class-thumb{width:56px;height:46px;background:linear-gradient(135deg,#6b5a50,#2d2d2d)}
.class-name{font-size:11px;color:var(--white);font-weight:600;margin-top:6px}
.class-date{font-size:10px;color:#888;margin-top:8px;display:flex;gap:6px;align-items:center}
.class-date i{width:10px;height:10px;border-radius:50%;background:#888;display:inline-block}

.copyright{top:4034px;height:48px;background:#111;font-size:11px;color:#888}
.copyright .left{left:68px;top:16px}
.copyright .right{right:68px;top:16px}
</style>
</head>
<body>
<div class="canvas">

<header class="site-header">
  <div class="abs brand">
    <div class="brand-name">Norvate Pastimes</div>
    <div class="brand-tag">Health, Wellness, Fitness, Consultants</div>
  </div>
  <nav class="abs main-nav">
    <a class="active">Home</a><a>Our Team</a><a>Testimonials</a><a>Health</a><a>Wellness</a><a>Fitness</a><a>Brimla Flex</a>
  </nav>
</header>

<section class="hero">
  <div class="abs hero-photo" role="img" aria-label="Two women training together in a gym studio"></div>
  <div class="abs hero-title">Norvate Pastimes</div>
  <div class="abs hero-sub">TRAINING STUDIO</div>
  <div class="abs hero-line">My style is elegant, sexy and strong.</div>
  <div class="abs btn-outline">Learn More</div>
</section>

<section class="about">
  <div class="abs about-dark">
    <div class="abs about-photo" role="img" aria-label="Athletic woman in black sportswear with fists raised"></div>
    <div class="abs story-small">My Transformation</div>
    <div class="abs story-big">STORY</div>
  </div>
  <div class="abs about-teal">
    <h2 class="abs about-title">ABOUT ME</h2>
    <div class="abs about-text">
      <p>Norvate Pastimes are leading consultants to the Health, Wellness and Fitness industry, with over 25 years experience working with some of the biggest global worldwide brands from equipment providers and facility operators to mass participation</p>
      <p>events and obstacle course races. Norvate Pastimes is a multi disciplined business specialising in helping brands grow through insight, strategy creation and valuable sector collaboration, recent clients include the exclusive distribution of Brimla Flex bodyweight training products for the UK and Ireland, exclusive distribution of fitness app Pulsewick Beats, Halvex Ridge Race, Ferncrest Dash, Quorra Cardio, Tevrin UK</p>
    </div>
    <div class="abs btn-outline">Start Today</div>
  </div>
</section>

<section class="bmi">
  <h2 class="abs section-head">Body and BMI Calculator</h2>
  <div class="abs bmi-card">
    <div class="abs tab tab-male">For Male</div>
    <div class="abs tab tab-female">For Female</div>
    <div class="abs field" style="left:26px;top:76px;width:146px">Enter Your Height</div>
    <div class="abs unit" style="left:180px;top:86px">FT</div>
    <div class="abs field" style="left:203px;top:76px;width:146px"></div>
    <div class="abs unit" style="left:358px;top:86px">IN</div>
    <div class="abs field" style="left:26px;top:130px;width:146px">Enter Your Age</div>
    <div class="abs unit" style="left:180px;top:140px">YRS</div>
    <div class="abs field" style="left:26px;top:187px;width:146px">Enter Your Weight</div>
    <div class="abs unit" style="left:180px;top:197px">LBS</div>
    <div class="abs field select" style="left:26px;top:242px">Enter You Pants Size</div>
    <div class="abs field select" style="left:26px;top:297px">Weight Goal</div>
    <div class="abs field select" style="left:26px;top:354px">Activity Level</div>
    <div class="abs info-dot" style="left:354px;top:364px"></div>
    <div class="abs btn-slant">START TODAY</div>
  </div>
  <div class="abs bmi-photo" role="img" aria-label="Two fit women posing and flexing their arms"></div>
</section>

<section class="services">
  <h2 class="abs section-head">We Provide Services</h2>
  <div class="abs service-card" style="left:54px">
    <div class="abs service-photo" style="background:linear-gradient(135deg,#8a6a55,#2a2a2a)" role="img" aria-label="Muscular man training with weights"></div>
    <div class="abs service-label">Health</div>
    <p class="abs service-text">Neque porro quisquam est, qui dolorem ipsum quia dolor sit amet, consectetur, adipis civelit sed quia modi.</p>
  </div>
  <div class="abs service-card" style="left:332px">
    <div class="abs service-photo" style="background:linear-gradient(135deg,#f0f0f0,#9aa4ad)" role="img" aria-label="Woman on an exercise bike in a bright gym"></div>
    <div class="abs service-label">Wellness</div>
    <p class="abs service-text">Neque porro quisquam est, qui dolorem ipsum quia dolor sit amet, consectetur, adipis civelit sed quia modi.</p>
  </div>
  <div class="abs service-card" style="left:610px">
    <div class="abs service-photo" style="background:linear-gradient(135deg,#cfe3ef,#7e9cb0)" role="img" aria-label="Woman stretching on a fitness mat"></div>
    <div class="abs service-label">Fitness</div>
    <p class="abs service-text">Neque porro quisquam est, qui dolorem ipsum quia dolor sit amet, consectetur, adipis civelit sed quia modi.</p>
  </div>
  <div class="abs service-card" style="left:888px">
    <div class="abs service-photo" style="background:linear-gradient(135deg,#b89a85,#4d4440)" role="img" aria-label="Trainer coaching a client with dumbbells"></div>
    <div class="abs service-label">Consultants</div>
    <p class="abs service-text">Neque porro quisquam est, qui dolorem ipsum quia dolor sit amet, consectetur, adipis civelit sed quia modi.</p>
  </div>
</section>

<section class="events">
  <h2 class="abs section-head">Upcoming Events</h2>
  <div class="abs head-rule"></div>

  <article class="abs event" style="left:57px">
    <div class="event-photo" style="background:linear-gradient(135deg,#c59a80,#5a4035)" role="img" aria-label="Man lifting a loaded barbell"></div>
    <div class="event-label">Powerlifting</div>
    <ul class="event-meta">
      <li><svg width="14" height="14" viewBox="0 0 14 14"><rect x="1" y="2" width="12" height="11" fill="none" stroke="#66c9b4" stroke-width="1.5"/><line x1="1" y1="5.5" x2="13" y2="5.5" stroke="#66c9b4" stroke-width="1.5"/></svg>February 12, 2014</li>
      <li><svg width="14" height="14" viewBox="0 0 14 14"><circle cx="7" cy="7" r="6" fill="none" stroke="#66c9b4" stroke-width="1.5"/><path d="M7 3.5V7h3" fill="none" stroke="#66c9b4" stroke-width="1.5"/></svg>11:30 - 13:30</li>
      <li><svg width="14" height="14" viewBox="0 0 14 14"><circle cx="7" cy="4.5" r="3" fill="none" stroke="#66c9b4" stroke-width="1.5"/><path d="M1.5 13c0-3 2.5-5 5.5-5s5.5 2 5.5 5" fill="none" stroke="#66c9b4" stroke-width="1.5"/></svg>Marla Quintrell</li>
    </ul>
  </article>

  <article class="abs event" style="left:340px">
    <div class="event-photo" style="background:linear-gradient(135deg,#4a3a32,#0f0f0f)" role="img" aria-label="Bodybuilder's muscular back"></div>
    <div class="event-label">Bodybuilding</div>
    <ul class="event-meta">
      <li><svg width="14" height="14" viewBox="0 0 14 14"><rect x="1" y="2" width="12" height="11" fill="none" stroke="#66c9b4" stroke-width="1.5"/><line x1="1" y1="5.5" x2="13" y2="5.5" stroke="#66c9b4" stroke-width="1.5"/></svg>February 12, 2014</li>
      <li><svg width="14" height="14" viewBox="0 0 14 14"><circle cx="7" cy="7" r="6" fill="none" stroke="#66c9b4" stroke-width="1.5"/><path d="M7 3.5V7h3" fill="none" stroke="#66c9b4" stroke-width="1.5"/></svg>11:30 - 13:30</li>
      <li><svg width="14" height="14" viewBox="0 0 14 14"><circle cx="7" cy="4.5" r="3" fill="none" stroke="#66c9b4" stroke-width="1.5"/><path d="M1.5 13c0-3 2.5-5 5.5-5s5.5 2 5.5 5" fill="none" stroke="#66c9b4" stroke-width="1.5"/></svg>Marla Quintrell</li>
    </ul>
  </article>

  <article class="abs event" style="left:623px">
    <div class="event-photo" style="background:linear-gradient(135deg,#6b4632,#1e1a18)" role="img" aria-label="Athlete training with a weighted ball"></div>
    <div class="event-label">Weight Training</div>
    <ul class="event-meta">
      <li><svg width="14" height="14" viewBox="0 0 14 14"><rect x="1" y="2" width="12" height="11" fill="none" stroke="#66c9b4" stroke-width="1.5"/><line x1="1" y1="5.5" x2="13" y2="5.5" stroke="#66c9b4" stroke-width="1.5"/></svg>February 12, 2014</li>
      <li><svg width="14" height="14" viewBox="0 0 14 14"><circle cx="7" cy="7" r="6" fill="none" stroke="#66c9b4" stroke-width="1.5"/><path d="M7 3.5V7h3" fill="none" stroke="#66c9b4" stroke-width="1.5"/></svg>11:30 - 13:30</li>
      <li><svg width="14" height="14" viewBox="0 0 14 14"><circle cx="7" cy="4.5" r="3" fill="none" stroke="#66c9b4" stroke-width="1.5"/><path d="M1.5 13c0-3 2.5-5 5.5-5s5.5 2 5.5 5" fill="none" stroke="#66c9b4" stroke-width="1.5"/></svg>Marla Quintrell</li>
    </ul>
  </article>

  <article class="abs event" style="left:906px">
    <div class="event-photo" style="background:linear-gradient(135deg,#5b7a98,#c9a38a)" role="img" aria-label="Toned midriff in yoga wear"></div>
    <div class="event-label">Yoga Training</div>
    <ul class="event-meta">
      <li><svg width="14" height="14" viewBox="0 0 14 14"><rect x="1" y="2" width="12" height="11" fill="none" stroke="#66c9b4" stroke-width="1.5"/><line x1="1" y1="5.5" x2="13" y2="5.5" stroke="#66c9b4" stroke-width="1.5"/></svg>February 12, 2014</li>
      <li><svg width="14" height="14" viewBox="0 0 14 14"><circle cx="7" cy="7" r="6" fill="none" stroke="#66c9b4" stroke-width="1.5"/><path d="M7 3.5V7h3" fill="none" stroke="#66c9b4" stroke-width="1.5"/></svg>11:30 - 13:30</li>
      <li><svg width="14" height="14" viewBox="0 0 14 14"><circle cx="7" cy="4.5" r="3" fill="none" stroke="#66c9b4" stroke-width="1.5"/><path d="M1.5 13c0-3 2.5-5 5.5-5s5.5 2 5.5 5" fill="none" stroke="#66c9b4" stroke-width="1.5"/></svg>Marla Quintrell</li>
    </ul>
  </article>
</section>

<section class="social">
  <h2 class="abs section-head">Our Social Sites</h2>

  <div class="abs social-col" style="left:90px">
    <div class="social-title"><i></i>FACEBOOK</div>
    <div class="widget">
      <div style="height:90px;background:linear-gradient(135deg,#3a3a3a,#8a8a8a)" role="img" aria-label="Page cover banner for DL Maren Fitness"></div>
      <div class="small" style="padding:6px 10px;font-weight:700">DL Maren Fitness</div>
      <div class="small" style="padding:0 10px 6px;color:#888">Be the first of your friends to like this</div>
      <div style="display:flex;gap:8px;padding:8px 10px;border-top:1px solid #eee">
        <div class="avatar"></div>
        <div class="small"><b>DL Maren Fitness</b><br>I'm so excited to be sharing my free book to help you go further.</div>
      </div>
      <div style="margin:6px 10px;height:200px;background:linear-gradient(135deg,#2f5f8f,#c99a80)" role="img" aria-label="Post photo of a smiling athlete"></div>
    </div>
  </div>

  <div class="abs social-col" style="left:452px">
    <div class="social-title"><i></i>INSTAGRAM</div>
    <div class="widget">
      <div style="display:flex;align-items:center;gap:14px;padding:12px 10px">
        <div style="width:54px;height:54px;border-radius:50%;background:#6a8ab0"></div>
        <div class="small"><b>dlmarenfit</b><br><span style="display:inline-block;margin-top:4px;padding:2px 10px;border:1px solid #66a3d6;color:#3d82c4">Follow</span></div>
      </div>
      <div class="small" style="display:flex;justify-content:space-around;text-align:center;padding:4px 0 10px;border-bottom:1px solid #eee"><span><b>591</b><br>posts</span><span><b>6,068</b><br>followers</span><span><b>864</b><br>following</span></div>
      <div class="ig-grid" style="margin-top:8px" role="img" aria-label="Grid of fitness photos">
        <span></span><span></span><span></span><span></span><span></span><span></span><span></span><span></span><span></span>
      </div>
    </div>
  </div>

  <div class="abs social-col" style="left:813px">
    <div class="social-title"><i></i>TWITTER</div>
    <div class="widget">
      <div class="small" style="padding:8px 10px;font-size:13px;font-weight:700;border-bottom:1px solid #eee">Tweets</div>
      <div class="tw-item"><div class="avatar"></div><div class="small"><b>Norvate Pastimes</b> @dlmarenfit<br>Trying new comments here today. Please read our updated terms and privacy policy.</div></div>
      <div class="tw-item"><div class="avatar"></div><div class="small"><b>Norvate Pastimes</b> @dlmarenfit<br>A new way for you to discover and buy products on the go.</div></div>
      <div class="tw-item"><div class="avatar"></div><div class="small"><b>Norvate Pastimes</b> @dlmarenfit<br>This is how much we love our new training range.</div></div>
      <div class="small" style="position:absolute;right:12px;bottom:10px;color:#3d82c4">View more</div>
    </div>
  </div>
</section>

<section class="subscribe">
  <div class="abs sub-label">Subscribe Now</div>
  <div class="abs sub-field">Enter Your Email</div>
  <div class="abs sub-plus">+</div>
  <div class="abs follow">Follow On: <span class="dot"></span><span class="dot"></span><span class="dot"></span><span class="dot"></span><span class="dot"></span><span class="dot"></span></div>
</section>

<footer class="site-footer">
  <div class="abs foot-brand">Norvate Pastimes</div>
  <div class="abs foot-tag">Health, Wellness, Fitness, Consultants</div>
  <p class="abs foot-about">consectetuer adipiscing adipielit Aenean loures commodo ligula eget dolor</p>
  <dl class="abs foot-contact">
    <dt>Address</dt><dd>Pellam Yard, 18 Orchard Row,<br>Lindmoor</dd>
    <dt style="margin-top:14px">Email</dt><dd style="margin-top:14px">hello@norvatepastimes.com</dd>
  </dl>
  <div class="abs foot-divider" style="left:381px"></div>
  <div class="abs foot-head" style="left:449px;top:86px">Opening Time</div>
  <ul class="abs hours">
    <li><span>Mon-Fri</span><span>00:00 am - 10:00pm</span></li>
    <li><span>Saturday</span><span>00:00 am - 10:00pm</span></li>
    <li><span>Sunday</span><span>00:00 am - 10:00pm</span></li>
  </ul>
  <div class="abs hours-note">Note: Fitness center is closed on holidays</div>
  <div class="abs foot-divider" style="left:770px"></div>
  <div class="abs foot-head" style="left:835px;top:86px">Up Comming Class</div>
  <div class="abs class-item" style="top:134px">
    <div class="class-thumb" role="img" aria-label="Class photo of a gym workout"></div>
    <div><div class="class-name">Sem Porta Mollis Parturi</div><div class="class-date"><i></i>12 July 2016</div></div>
  </div>
  <div class="abs class-item" style="top:204px">
    <div class="class-thumb" role="img" aria-label="Class photo of weight training"></div>
    <div><div class="class-name">Sem Porta Mollis Parturi</div><div class="class-date"><i></i>12 July 2016</div></div>
  </div>
</footer>

<div class="abs copyright" style="position:absolute;left:0;width:1200px">
  <div class="abs left">© Copyright 2016. All rights reserved.</div>
  <div class="abs right">Terms Of Use &nbsp;|&nbsp; Privacy &amp; Security Statements</div>
</div>

</div>
</body>
</html>
```